Service Menu refresh 2018 Update of menu pricing

We currently have service menus as attached. We will be updating our look via our homepage image, our service menu and our in-house beverage and treatment menu.
We are a natural and sustainable hair salon group and moving more towards head spa which consists of treatments, beauty, tanning as well as your traditional hair services. Our imagery needs to reflect our efforts in spa treatments in the hair and scalp area and use natural materials and colours reflecting sustainability.
Velin is the brand we stock and promote.

Target Market(s)

Men or women interesting in personal maintenance with natural and organic products and using sustainable practises

Industry/Entity Type

Hair And Beauty

Font styles to use
Sans Serif
Other font styles liked:
• Arial or Helvetica

Colors
9acb3c
abd037
cadf82
ffffff

Requirements
Must have
• Name on the front cover, locations on back cover
Nice to have
• Prestige feel, reflect male and female clients
Should not have
• Bold artificial writing or any type of cartoon images.
• Same images as existing menu.

```html
<!DOCTYPE html>
<html lang="en">
<head>
<meta charset="utf-8">
<title>Fernleaf Hair Studios – Service Menu</title>
<link rel="stylesheet" href="https://fonts.googleapis.com/css2?family=Cinzel:wght@400&family=Open+Sans:wght@400;600&family=Catamaran:wght@500;700&display=swap">
<style>
:root{
  --bg:#eeeeee;
  --paper:#ffffff;
  --mint:#5ef08e;
  --mint-pale:#eaf6e6;
  --leaf:#9acb3c;
  --lime:#abd037;
  --sage:#cadf82;
  --forest:#1f4a10;
  --olive:#5b8a22;
  --ink:#3a3a3a;
  --dark:#1a1a1a;
}
*{margin:0;padding:0;box-sizing:border-box}
html,body{width:1200px;height:494px;overflow:hidden;background:var(--bg)}
.canvas{position:relative;width:1200px;height:494px}
.card{position:absolute;top:26px;height:380px;box-shadow:0 10px 18px rgba(0,0,0,.18)}

/* back cover */
.back{left:52px;width:538px;background:var(--paper);font-family:"Open Sans",Arial,sans-serif}
.pattern-panel{position:absolute;left:0;top:0;width:166px;height:380px;
  background:linear-gradient(160deg,#e9efd6 0%,#d7e4b0 45%,#e4ecc9 100%)}
.pattern-edge{position:absolute;right:0;top:0;width:12px;height:380px;
  background:linear-gradient(180deg,#dfe9c0,#cfe09a,#e2eac8)}
.divider{position:absolute;left:170px;top:0;width:2px;height:380px;background:var(--sage)}
.brand-plate{position:absolute;left:28px;top:272px;width:206px;height:66px;background:var(--dark);
  border:1px solid var(--lime);border-radius:2px;display:flex;align-items:center;gap:9px;padding-left:16px}
.brand-dot{width:14px;height:14px;border-radius:50%;background:var(--leaf)}
.brand-name{font-family:"Open Sans",Arial,sans-serif;font-weight:400;font-size:15px;color:var(--paper);line-height:1.15}
.quote{position:absolute;left:250px;top:26px;width:280px;text-align:center;font-family:"Cinzel",serif;
  font-size:10.5px;line-height:17px;color:var(--lime);letter-spacing:.3px}
.location{position:absolute;left:263px;border-left:2px solid var(--leaf);padding-left:13px;font-size:7px;line-height:9.6px;color:var(--ink)}
.location h3{font-size:7.4px;font-weight:600;color:var(--leaf);margin-bottom:2px}
.web{position:absolute;left:278px;top:354px;font-size:6.8px;font-weight:600;color:var(--forest)}

/* price menu */
.menu{left:630px;width:542px;font-family:"Catamaran",Arial,sans-serif;
  background:linear-gradient(135deg,#f3faf1 0%,#e6f4e2 50%,#f1f8ee 100%)}
.menu-texture{position:absolute;left:0;top:38px;width:542px;height:342px;
  background:radial-gradient(circle at 70% 55%,rgba(154,203,60,.12),transparent 60%)}
.menu-head{position:absolute;left:0;top:0;width:542px;height:38px;background:var(--mint)}
.menu-head span{position:absolute;top:11px;font-size:11.5px;font-weight:700;color:var(--paper);letter-spacing:.3px}
.row{position:absolute;font-size:9.4px;color:var(--olive);font-weight:500}
.row.group{font-weight:700;color:var(--forest);font-size:9.6px}
.row.underline{border-bottom:1px solid var(--forest)}
.price{position:absolute;font-size:9.4px;font-weight:700;color:var(--forest)}
.note{position:absolute;left:288px;font-size:8.6px;color:var(--olive)}
.fine{position:absolute;left:288px;top:330px;width:246px;font-size:6px;line-height:8px;color:var(--forest)}
</style>
</head>
<body>
<div class="canvas">

  <section class="card back">
    <div class="pattern-panel" role="img" aria-label="Pattern of drawn leaves in soft greens"></div>
    <div class="divider"></div>
    <div class="pattern-edge" role="img" aria-label="Strip of drawn leaf pattern"></div>

    <div class="brand-plate">
      <span class="brand-dot"></span>
      <span class="brand-name">Fernleaf Hair Studios</span>
    </div>

    <p class="quote">“ Living a more natural and organic life is a<br>philosophy not just a product certification ”</p>

    <div class="location" style="top:63px">
      <h3>HOLLIN VALE</h3>
      Shop 12 Hollin Vale Plaza,<br>Reed St, Hollin Vale<br>+61 (07) 5550 0141<br>hollinvale@fernleafhair.example
    </div>
    <div class="location" style="top:120px">
      <h3>ASHGROVE NORTH</h3>
      Shop 40 Ashgrove Village, Miller Road, Ashgrove North<br>+61 (07) 5550 0172<br>ashgrove@fernleafhair.example
    </div>
    <div class="location" style="top:169px">
      <h3>MARROW CREEK</h3>
      Shop 208 Marrow Creek Shopping Centre, Tallow<br>Rd Marrow Creek.<br>+61 (07) 5550 0193<br>marrowcreek@fernleafhair.example
    </div>
    <div class="location" style="top:230px">
      <h3>BAYWATER LAKES</h3>
      Shop 75 Baywater Lakes Mall,<br>Harbour St, Baywater Lakes<br>+61 (07) 5550 0124<br>baywater@fernleafhair.example
    </div>
    <div class="location" style="top:296px">
      <h3>EASTBROOK CLINIC</h3>
      Linden St, Eastbrook QLD 4000<br>+61 (07) 5550 0165<br>eastbrook@fernleafhair.example
    </div>
    <p class="web">WWW.FERNLEAFHAIR.EXAMPLE</p>
  </section>

  <section class="card menu">
    <div class="menu-texture" role="img" aria-label="Faint drawn leaf pattern across the menu"></div>
    <div class="menu-head">
      <span style="left:19px">CUT &amp; BLOWDRY</span>
      <span style="left:160px">S</span><span style="left:186px">M</span><span style="left:214px">L</span><span style="left:238px">XL</span>
      <span style="left:288px">COLOUR</span>
      <span style="left:422px">S</span><span style="left:451px">M</span><span style="left:479px">L</span><span style="left:506px">XL</span>
    </div>

    <!-- cut & blowdry -->
    <span class="row group underline" style="left:28px;top:44px">LADIES FRINGE</span>
    <span class="price" style="left:154px;top:44px">$77</span><span class="price" style="left:181px;top:44px">$88</span><span class="price" style="left:207px;top:44px">$99</span><span class="price" style="left:234px;top:44px">$110</span>
    <span class="row" style="left:28px;top:60px">Trim</span><span class="price" style="left:154px;top:60px">$25</span>
    <span class="row" style="left:28px;top:73px">Restyle</span><span class="price" style="left:154px;top:73px">$35</span>
    <span class="row group" style="left:28px;top:89px">MENS</span>
    <span class="row" style="left:28px;top:102px">Single clipper</span><span class="price" style="left:154px;top:102px">$28</span>
    <span class="row" style="left:28px;top:116px">Style cut</span><span class="price" style="left:154px;top:116px">$42</span>
    <span class="row group" style="left:28px;top:136px">CHILDREN</span>
    <span class="row" style="left:28px;top:153px">10 and under</span><span class="price" style="left:154px;top:153px">$24</span>
    <span class="row" style="left:28px;top:166px">11-16 Male</span><span class="price" style="left:154px;top:166px">$32</span>
    <span class="row" style="left:28px;top:182px">11-16 Female</span><span class="price" style="left:154px;top:182px">$48</span>
    <span class="row" style="left:28px;top:197px">add a wash</span><span class="price" style="left:154px;top:197px">$5</span>
    <span class="row group" style="left:28px;top:219px">BLOWDRY</span>
    <span class="price" style="left:154px;top:219px">$77</span><span class="price" style="left:181px;top:219px">$88</span><span class="price" style="left:207px;top:219px">$99</span><span class="price" style="left:234px;top:219px">$110</span>
    <span class="row" style="left:28px;top:234px">Shampoo &amp; dry off</span><span class="price" style="left:154px;top:234px">$25</span>
    <span class="row group" style="left:28px;top:261px">TREATMENTS</span>
    <span class="row" style="left:28px;top:275px">deep treatment</span><span class="price" style="left:154px;top:275px">$35</span>
    <span class="row" style="left:28px;top:290px">Head.Spa ritual</span><span class="price" style="left:154px;top:290px">$65</span>
    <span class="row group" style="left:28px;top:310px">UP STYLE</span>
    <span class="row" style="left:28px;top:324px">45 minutes</span><span class="price" style="left:154px;top:324px">$85</span>
    <span class="row" style="left:28px;top:341px">60 minutes</span><span class="price" style="left:154px;top:341px">$120</span>

    <!-- colour -->
    <span class="row group" style="left:288px;top:44px">REGROWTH</span><span class="price" style="left:418px;top:40px">$83</span>
    <span class="row group underline" style="left:288px;top:61px">FULL COLOUR TINT</span>
    <span class="price" style="left:418px;top:58px">$125</span><span class="price" style="left:448px;top:58px">$145</span><span class="price" style="left:477px;top:58px">$165</span><span class="price" style="left:505px;top:58px">$185</span>
    <span class="row group underline" style="left:288px;top:78px">REGROWTH LIGHTENING*</span>
    <span class="price" style="left:418px;top:75px">$165</span><span class="price" style="left:448px;top:75px">$189</span><span class="price" style="left:477px;top:75px">$209</span><span class="price" style="left:505px;top:75px">$229</span>
    <span class="row group" style="left:288px;top:94px">BALAYAGE/OMBRE*</span>
    <span class="price" style="left:448px;top:91px">$275</span><span class="price" style="left:477px;top:91px">$375</span><span class="price" style="left:505px;top:91px">$475</span>
    <span class="row group" style="left:288px;top:117px">PURE GLOSS</span>
    <span class="row" style="left:288px;top:130px;color:var(--forest)">REGROWTH</span><span class="price" style="left:418px;top:130px">$99</span>
    <span class="row" style="left:288px;top:140px;color:var(--forest)">FULL COLOUR TINT</span>
    <span class="price" style="left:418px;top:140px">$155</span><span class="price" style="left:448px;top:140px">$175</span><span class="price" style="left:477px;top:140px">$195</span><span class="price" style="left:505px;top:140px">$205</span>
    <span class="row group" style="left:288px;top:162px">FOILS*</span>
    <span class="row" style="left:288px;top:175px;color:var(--forest)">SINGLE*</span>
    <span class="price" style="left:418px;top:175px">$11</span><span class="price" style="left:448px;top:175px">$13</span><span class="price" style="left:477px;top:175px">$17</span><span class="price" style="left:505px;top:175px">$22</span>
    <span class="row" style="left:288px;top:187px;color:var(--forest)">1/4 HEAD</span>
    <span class="price" style="left:418px;top:187px">$135</span><span class="price" style="left:448px;top:187px">$155</span><span class="price" style="left:477px;top:187px">$175</span><span class="price" style="left:505px;top:187px">$195</span>
    <span class="row" style="left:288px;top:200px;color:var(--forest)">1/2 HEAD</span>
    <span class="price" style="left:418px;top:200px">$185</span><span class="price" style="left:448px;top:200px">$205</span><span class="price" style="left:477px;top:200px">$235</span><span class="price" style="left:505px;top:200px">$265</span>
    <span class="row" style="left:288px;top:212px;color:var(--forest)">FULL HEAD</span>
    <span class="price" style="left:418px;top:212px">$235</span><span class="price" style="left:448px;top:212px">$265</span><span class="price" style="left:477px;top:212px">$315</span><span class="price" style="left:505px;top:212px">$355</span>
    <span class="row group" style="left:288px;top:237px">STRAIGHT</span>
    <span class="row group" style="left:288px;top:249px;line-height:11px">KERATIN STRAIGHTENING<br>&nbsp;SYSTEM</span>
    <span class="price" style="left:418px;top:249px">$365</span><span class="price" style="left:448px;top:249px">$445</span><span class="price" style="left:477px;top:249px">$535</span><span class="price" style="left:505px;top:249px">$565</span>

    <span class="note" style="top:289px">*Includes colour match &amp; toner</span>
    <span class="note" style="top:302px">*Minimum 6 foils without colour</span>
    <span class="note" style="top:315px">*Minimum charge on a Sunday is $40</span>
    <p class="fine">Pricing is indicative of average products used and time taken for each service. You will ALWAYS receive a firm price after your consultation. S to the jaw line I M to the collarbone I L to the bra strap I XL past bra strap</p>
  </section>

</div>
</body>
</html>
```